E Marketing - Quill Flyer

Our product is an E Marketing campaign for business.We have called the product Quill. Benefits to Business are:
1. Direct communications to qualified clients;
2. Generate new leads;
2. Drive traffic to your website;
3. Unlimited campaigns.

We want to have a special offer whereby the client signs on for twelve months and recieves two months free. The cost of the product is $550 for the templeate as a one off fee and $90 per month.The designer can deciede whether the cost should feature in the flyer.
Our website for reference is www.harborvistagroupwerks.com.au

Target Market(s)

Business who currently have a website and would like to drive more traffic. Businessess who want to talk directly to thier clients. Business who want to increase sales.

Industry/Entity Type

Marketing

Requirements
Must have
• The brochure should be a single page, not cluttered and clear. It should reflect our corporate colours. The brochure should highlight the name Quill.

```html
<!DOCTYPE html>
<html lang="en">
<head>
<meta charset="utf-8">
<title>Quill Email Marketing Flyer</title>
<link rel="stylesheet" href="https://fonts.googleapis.com/css2?family=PT+Sans:wght@400;700&display=swap">
<style>
  :root {
    --navy: #163f73;
    --navy-deep: #133a6a;
    --panel-top: #1c4a80;
    --panel-bottom: #466f9e;
    --band-light: #a9d4ee;
    --band-mid: #6fb1dc;
    --sky-deep: #2c6fb8;
    --sky-mid: #6fa6da;
    --sky-light: #d6e7f5;
    --tick: #7fb0d8;
    --white: #ffffff;
  }
  * { margin: 0; padding: 0; box-sizing: border-box; }
  html, body { width: 848px; height: 1200px; overflow: hidden; background: var(--white); }
  body { font-family: "PT Sans", Arial, sans-serif; }
  .flyer { position: relative; width: 848px; height: 1200px; overflow: hidden; background: var(--white); }

  .headline { position: absolute; top: 22px; left: 0; width: 848px; color: var(--navy); font-size: 34.5px; letter-spacing: -0.6px; line-height: 1.05; }
  .headline strong { font-weight: 700; }
  .headline .line-one { position: absolute; left: 78px; top: 0; white-space: nowrap; }
  .headline .line-two { position: absolute; right: 88px; top: 34px; white-space: nowrap; }

  .band { position: absolute; left: 0; width: 848px; background: linear-gradient(180deg, var(--band-light), var(--band-mid)); }
  .band-top { top: 125px; height: 48px; }
  .band-top .tagline { position: absolute; right: 90px; top: 5px; color: var(--white); font-weight: 700; font-size: 30px; letter-spacing: -0.6px; white-space: nowrap; }
  .band-bottom { top: 1152px; height: 48px; }

  .benefits { position: absolute; top: 173px; left: 0; width: 848px; height: 316px; background: linear-gradient(100deg, var(--panel-top) 0%, var(--panel-bottom) 100%); color: var(--white); }
  .benefits h1 { position: absolute; left: 68px; top: 28px; font-size: 37px; font-weight: 700; letter-spacing: -1px; padding-bottom: 4px; border-bottom: 3px solid var(--band-light); width: 440px; white-space: nowrap; }
  .benefits .subhead { position: absolute; left: 68px; top: 91px; font-size: 18.6px; font-weight: 700; letter-spacing: -0.3px; white-space: nowrap; }
  .benefit-list { list-style: none; }
  .benefit-list li { position: absolute; font-size: 16.6px; font-weight: 700; white-space: nowrap; display: flex; align-items: center; gap: 14px; }
  .benefit-list svg { width: 24px; height: 18px; flex: none; }

  .offer { position: absolute; top: 488px; left: 0; width: 848px; height: 442px; }
  .sky { position: absolute; inset: 0; background: linear-gradient(160deg, var(--sky-deep) 0%, var(--sky-mid) 55%, var(--sky-light) 100%); }
  .offer-text { position: absolute; color: var(--white); font-weight: 700; white-space: nowrap; text-shadow: 0 0 12px rgba(20,60,120,0.55), 0 2px 4px rgba(20,60,120,0.4); letter-spacing: -2px; line-height: 1; }
  .sign-on { left: 103px; top: 40px; font-size: 58px; }
  .months { left: 276px; top: 96px; font-size: 92px; letter-spacing: -3px; }
  .two { left: 180px; top: 160px; font-size: 175px; letter-spacing: 0; }
  .receive { left: 296px; top: 180px; font-size: 55px; }
  .for-free { left: 292px; top: 226px; font-size: 93px; letter-spacing: -3px; }
  .call-ask { right: 92px; top: 350px; font-size: 42px; letter-spacing: -1.2px; }

  .contact-panel { position: absolute; top: 930px; left: 0; width: 848px; height: 222px; background: var(--navy-deep); color: var(--white); }
  .company-name { position: absolute; left: 290px; top: 32px; display: flex; align-items: center; gap: 10px; font-size: 22px; font-weight: 700; letter-spacing: -0.3px; white-space: nowrap; }
  .company-name .mark { width: 24px; height: 24px; background: var(--white); }
  .contact { position: absolute; left: 540px; top: 28px; font-size: 13px; line-height: 17px; font-style: normal; }
  .contact .call { font-size: 21px; font-weight: 700; line-height: 26px; margin-bottom: 2px; }
  .contact .gap { height: 17px; }

  .price-badge { position: absolute; left: 66px; top: 846px; width: 188px; height: 188px; }
  .price-badge svg { position: absolute; inset: 0; width: 100%; height: 100%; transform: rotate(-8deg); filter: drop-shadow(0 3px 5px rgba(0,0,0,0.35)); }
  .price-badge p { position: absolute; left: 0; top: 64px; width: 100%; text-align: center; color: var(--white); font-weight: 700; line-height: 0.95; text-shadow: 0 1px 3px rgba(20,60,120,0.6); }
  .price-badge .amount { font-size: 31px; letter-spacing: -0.5px; }
  .price-badge .per { font-size: 24px; }
</style>
</head>
<body>
<main class="flyer">
  <header class="headline">
    <p class="line-one">Are you using the <strong>Marketing Channel</strong></p>
    <p class="line-two">which has the <strong>highest ROI</strong></p>
  </header>

  <div class="band band-top"><p class="tagline">We can show you how</p></div>

  <section class="benefits">
    <h1>QUILL - EMAIL MARKETING</h1>
    <p class="subhead">THE SUPER-EASY WAY TO KEEP IN TOUCH WITH PROSPECTS AND CUSTOMERS.</p>
    <ul class="benefit-list">
      <li style="left:66px;top:159px"><svg viewBox="0 0 24 18"><path d="M2 9 L9 16 L22 2" fill="none" stroke="var(--tick)" stroke-width="5" stroke-linejoin="round"/></svg>Direct Communications to Qualified Clients</li>
      <li style="left:459px;top:159px"><svg viewBox="0 0 24 18"><path d="M2 9 L9 16 L22 2" fill="none" stroke="var(--tick)" stroke-width="5" stroke-linejoin="round"/></svg>Drive Traffic to Your Website</li>
      <li style="left:66px;top:198px"><svg viewBox="0 0 24 18"><path d="M2 9 L9 16 L22 2" fill="none" stroke="var(--tick)" stroke-width="5" stroke-linejoin="round"/></svg>Generate New Leads</li>
      <li style="left:459px;top:199px"><svg viewBox="0 0 24 18"><path d="M2 9 L9 16 L22 2" fill="none" stroke="var(--tick)" stroke-width="5" stroke-linejoin="round"/></svg>Unlimited Campaigns</li>
      <li style="left:66px;top:236px"><svg viewBox="0 0 24 18"><path d="M2 9 L9 16 L22 2" fill="none" stroke="var(--tick)" stroke-width="5" stroke-linejoin="round"/></svg>Free reports that track sends, opens, clicked links and more.</li>
    </ul>
  </section>

  <section class="offer">
    <div class="sky" role="img" aria-label="Photograph of a bright blue sky with white clouds"></div>
    <p class="offer-text sign-on">Sign on for</p>
    <p class="offer-text months">12 months</p>
    <p class="offer-text two">2</p>
    <p class="offer-text receive">receive</p>
    <p class="offer-text for-free">for free</p>
    <p class="offer-text call-ask">Call and ask us how</p>
  </section>

  <footer class="contact-panel">
    <p class="company-name"><span class="mark"></span>Harbor Vista Group</p>
    <address class="contact">
      <p class="call">call (03) 5550 1846</p>
      <p>PO Box 2210, Harbourton Vic 3999</p>
      <p>14 Marlow St Harbourton</p>
      <div class="gap"></div>
      <p>P : +61 3 5550 1846</p>
      <p>F : +61 3 5550 1847</p>
      <p>info@harborvistagroupwerks.com.au</p>
      <p>www.harborvistagroupwerks.com.au</p>
    </address>
  </footer>

  <div class="price-badge">
    <svg viewBox="0 0 200 200" aria-hidden="true">
      <defs>
        <radialGradient id="badgeFill" cx="40%" cy="35%" r="70%">
          <stop offset="0" stop-color="#b9def2"/>
          <stop offset="1" stop-color="#5fa3d3"/>
        </radialGradient>
      </defs>
      <polygon fill="url(#badgeFill)" points="195,100 180.4,116 187.8,136.4 168.1,145.6 167.2,167.2 145.6,168.1 136.4,187.8 116,180.4 100,195 84,180.4 63.6,187.8 54.4,168.1 32.8,167.2 31.9,145.6 12.2,136.4 19.6,116 5,100 19.6,84 12.2,63.6 31.9,54.4 32.8,32.8 54.4,31.9 63.6,12.2 84,19.6 100,5 116,19.6 136.4,12.2 145.6,31.9 167.2,32.8 168.1,54.4 187.8,63.6 180.4,84"/>
    </svg>
    <p><span class="amount">Only $90</span><br><span class="per">per month!</span></p>
  </div>

  <div class="band band-bottom"></div>
</main>
</body>
</html>
```